Wordpress Website for electrician

I'm looking for an easy to maintain website for my electrical contracting business. Need a professional and appealing site.
Im wanting a website where clients can come on and look at services we offer, case studies and advertise our services.
Colours I'm wanting to incorporate are green, white, black and grey
I'm wanting a big slide show on main page where I can place advertising etc.
Menu is to include home, services, our work, specials, energy efficiency and contact
My existing site is www.trelwirefix.com.au
Updates
looking for something with a similar layout to this website
Target Market(s)
Businesses
Industry/Entity Type
Electrician
Look and feel

```html
<!DOCTYPE html>
<html lang="en">
<head>
<meta charset="utf-8">
<title>trelwirefix – electrical contractor</title>
<link href="https://fonts.googleapis.com/css2?family=Source+Sans+3:ital,wght@0,400;0,600;0,700;1,400&family=PT+Sans+Narrow:wght@400;700&display=swap" rel="stylesheet">
<style>
:root{
  --green:#3db04b;
  --green-dark:#2f9a3c;
  --ink:#333;
  --text:#555;
  --muted:#777;
  --line:#ddd;
  --panel:#ececec;
  --footer:#5a5a5a;
  --footer-deep:#4a4a4a;
  --white:#fff;
}
*{box-sizing:border-box;margin:0;padding:0}
html,body{width:803px;height:1200px;overflow:hidden;background:var(--white)}
body{position:relative;font-family:"Source Sans 3",sans-serif;color:var(--text);font-size:9px;line-height:1.6}
.abs{position:absolute}
.brand{left:60px;top:30px;display:flex;align-items:center;gap:7px}
.brand-dot{width:14px;height:14px;border-radius:50%;background:var(--green)}
.brand-name{font-size:21px;font-weight:600;color:var(--ink);letter-spacing:.3px}
.brand-tag{left:81px;top:58px;font-size:7px;color:var(--muted)}
.search{left:594px;top:21px;width:151px;height:22px;border:1px solid #ccc;border-radius:2px;font-size:8px;font-style:italic;color:#aaa;padding:4px 5px}
.search svg{position:absolute;right:6px;top:5px}
.nav{left:382px;top:60px;display:flex;gap:0;font-family:"PT Sans Narrow",sans-serif;font-size:11.5px;color:var(--ink)}
.nav span{padding:0 10.5px;line-height:21px}
.nav .on{background:var(--green);color:var(--white);padding:0 7px;margin-right:3px}
.offer{left:57px;top:110px;width:211px;height:250px;border:1px solid var(--line)}
.offer-head{background:var(--green);color:var(--white);font-family:"PT Sans Narrow",sans-serif;font-size:15px;padding:7px 10px;height:33px}
.offer-img{position:absolute;left:40px;top:46px;width:125px;height:128px;background:linear-gradient(135deg,#7a3fa0,#b58fce 55%,#e8e8e8);border-radius:3px}
.offer-title{position:absolute;left:9px;top:183px;font-family:"PT Sans Narrow",sans-serif;font-size:15px;color:var(--green)}
.offer-sub{position:absolute;left:9px;top:205px;font-size:9.5px;color:var(--ink)}
.offer-price{position:absolute;left:136px;top:188px;font-family:"PT Sans Narrow",sans-serif;font-size:21px;color:var(--green)}
.offer-price small{font-size:11px;color:var(--ink)}
.offer-link{position:absolute;left:0;right:0;top:228px;text-align:center;font-size:9.5px;color:var(--ink)}
.slider{left:280px;top:111px;width:464px;height:249px;background:radial-gradient(ellipse at 62% 40%,#f4f4ee 0%,#bdbdb5 25%,#3a3a3a 55%,#0c0c0c 80%)}
.slider-arrows{position:absolute;right:9px;bottom:10px;display:flex;gap:3px}
.slider-arrows span{width:19px;height:19px;background:#444;display:flex;align-items:center;justify-content:center}
.welcome{left:58px;top:381px;width:687px;text-align:center}
.welcome h1{font-family:"PT Sans Narrow",sans-serif;font-weight:400;font-size:16px;color:var(--green);margin-bottom:5px}
.welcome p{font-size:9px;line-height:16.8px;color:var(--text)}
.btn{top:473px;height:25px;color:var(--white);font-family:"PT Sans Narrow",sans-serif;font-size:11px;display:flex;align-items:center;gap:6px;padding:0 9px}
.btn i{width:10px;height:10px;border-radius:50%;background:var(--white);display:inline-flex;align-items:center;justify-content:center}
.btn-quote{left:272px;width:109px;background:var(--green)}
.btn-audit{left:409px;width:118px;background:#3d3d3d}
.service{top:537px;width:200px;text-align:center}
.service .disc{width:96px;height:96px;margin:0 auto;border-radius:50%;background:radial-gradient(circle at 50% 40%,#fff 0%,#f2f2f2 55%,#d9d9d9 100%);box-shadow:0 6px 10px rgba(0,0,0,.1);display:flex;align-items:center;justify-content:center}
.service h2{font-family:"Source Sans 3",sans-serif;font-weight:600;font-size:14px;color:var(--ink);margin-top:15px}
.service p{font-size:9px;line-height:14.5px;letter-spacing:.2px;margin-top:2px}
.divider{left:57px;top:744px;width:688px;height:1px;background:linear-gradient(90deg,transparent,#ddd 15%,#ddd 85%,transparent)}
.col-head{top:765px;font-family:"PT Sans Narrow",sans-serif;font-size:14px;color:var(--green)}
.specials-img{left:59px;top:791px;width:203px;height:108px;background:radial-gradient(circle at 62% 52%,#fffbe8 0%,#e7d29a 18%,#a0724e 38%,#1f4f8f 70%,#163d73 100%)}
.specials-text{left:59px;top:909px;width:205px;font-size:8.6px;line-height:14.5px}
.news{left:304px;width:215px;height:60px}
.news .thumb{position:absolute;left:0;top:0;width:66px;height:60px;border:2px solid #eee;background:linear-gradient(135deg,#e9eef3,#9fb6c9)}
.news h3{position:absolute;left:73px;top:-4px;font-weight:400;font-size:10px;color:var(--green)}
.news p{position:absolute;left:73px;top:11px;font-size:8.3px;line-height:14.5px;color:var(--text)}
.quote-box{left:552px;top:797px;width:196px;height:94px;background:var(--panel);padding:9px 8px 8px 14px;font-style:italic;font-size:8.3px;line-height:16px;color:#555}
.quote-tail{left:686px;top:891px}
.portrait{left:552px;top:922px;width:72px;height:66px;background:linear-gradient(160deg,#6f7b88,#c8a58d 50%,#3b4652)}
.cite{left:637px;top:922px;width:115px;font-size:8.5px;font-weight:600;line-height:14.5px;color:var(--ink)}
.cite-name{left:637px;top:958px;display:flex;align-items:center;gap:6px;font-size:8.5px;font-weight:600;color:var(--ink)}
.footer{left:0;top:1027px;width:803px;height:129px;background:var(--footer);color:#eee}
.footer-base{left:0;top:1156px;width:803px;height:44px;background:var(--footer-deep);color:#eee;font-size:8.5px}
.fcol{position:absolute;top:9px;font-size:8.5px;line-height:19.3px}
.fcol b{font-weight:400;display:block}
.accred{position:absolute;left:470px;top:9px;width:126px;text-align:center;font-size:8.5px;line-height:16px}
.badge{width:60px;height:60px;margin:6px auto 0;background:#4aa3d8;border-radius:50%}
.social{position:absolute;left:634px;top:9px;font-size:10px}
.social .row{display:flex;align-items:center;gap:10px;margin-top:8px}
.social .sq{width:19px;height:19px;border-radius:3px}
</style>
</head>
<body>

<header>
  <div class="abs brand"><span class="brand-dot"></span><span class="brand-name">trelwirefix</span></div>
  <div class="abs brand-tag">electrical contractor</div>
  <div class="abs search">Search..
    <svg width="10" height="10" viewBox="0 0 10 10"><circle cx="4" cy="4" r="3" fill="none" stroke="#999" stroke-width="1.3"/><line x1="6.2" y1="6.2" x2="9" y2="9" stroke="#999" stroke-width="1.4"/></svg>
  </div>
  <nav class="abs nav"><span class="on">HOME</span><span>ABOUT</span><span>SERVICES</span><span>OUR WORK</span><span>SPECIALS</span><span>CONTACT</span></nav>
</header>

<section class="abs offer">
  <div class="offer-head">SPECIAL OFFER</div>
  <div class="offer-img" role="img" aria-label="Boxed LED downlight kit with bulb"></div>
  <div class="offer-title">LED LIGHTS</div>
  <div class="offer-sub">Supplied and Installed</div>
  <div class="offer-price">$33 <small>Each</small></div>
  <div class="offer-link">Click here for more details</div>
</section>

<section class="abs slider" role="img" aria-label="Glowing light bulb on a dark background">
  <div class="slider-arrows">
    <span><svg width="6" height="9" viewBox="0 0 6 9"><path d="M5 1 1 4.5 5 8" fill="none" stroke="#fff" stroke-width="1.3"/></svg></span>
    <span><svg width="6" height="9" viewBox="0 0 6 9"><path d="M1 1 5 4.5 1 8" fill="none" stroke="#fff" stroke-width="1.3"/></svg></span>
  </div>
</section>

<section class="abs welcome">
  <h1>Welcome to our website</h1>
  <p>Lorem ipsum dolor sit amet conse ctetur adipisicing elit, sed do eiusmod tempor incididunt ut labore et dolore magna aliqua. Ut enim ad minim veniam, quis no strud exercitation ullamco laboris nisi ut aliquip ex ea commodo consequat. Lorem ipsum dolor sit amet conse ctietur adipisicing elit, sed do eiusmod te mpor incididunt ut labore et dolore magna aliqua. Ut enim ad minim veniam, quis nostrud exercitation ullamco laboris nisi ut aliquip ex ea com</p>
</section>

<a class="abs btn btn-quote">REQUEST QUOTE <i><svg width="6" height="6" viewBox="0 0 6 6"><path d="M0 3h5M3 1l2 2-2 2" fill="none" stroke="#3db04b" stroke-width="1.2"/></svg></i></a>
<a class="abs btn btn-audit">BOOK AUDIT NOW <i><svg width="6" height="6" viewBox="0 0 6 6"><path d="M0 3h5M3 1l2 2-2 2" fill="none" stroke="#3d3d3d" stroke-width="1.2"/></svg></i></a>

<section class="abs service" style="left:77px">
  <div class="disc"><svg width="40" height="44" viewBox="0 0 40 44"><rect x="10" y="2" width="5" height="12" fill="#3db04b"/><rect x="25" y="2" width="5" height="12" fill="#3db04b"/><path d="M4 14h32v8c0 8-7 12-12 12v8h-8v-8C11 34 4 30 4 22z" fill="#3db04b"/></svg></div>
  <h2>Electrical Contracting</h2>
  <p>Lorem ipsum dolor sit amet adipis ing elit.Morbi ut elipsum tristique acc umsan. Morbi ut elit utipsum tristiquea Pellentesque habitant morbi.</p>
</section>
<section class="abs service" style="left:296px">
  <div class="disc"><svg width="26" height="52" viewBox="0 0 26 52"><rect x="3" y="2" width="20" height="6" rx="3" fill="#3db04b"/><rect x="3" y="10" width="20" height="6" rx="3" fill="#3db04b"/><rect x="3" y="18" width="20" height="6" rx="3" fill="#3db04b"/><path d="M3 27h20l-3 10H6z" fill="#3db04b"/><rect x="8" y="39" width="10" height="10" rx="2" fill="#3db04b"/></svg></div>
  <h2>Energy Efficiency</h2>
  <p>Lorem ipsum dolor sit amet adipis ing elit.Morbi ut elipsum tristique acc umsan. Morbi ut elit utipsum tristiquea Pellentesque habitant morbi.</p>
</section>
<section class="abs service" style="left:524px">
  <div class="disc"><svg width="30" height="48" viewBox="0 0 30 48"><path d="M12 2 4 24h10l-4 22 16-28H16l6-16z" fill="none" stroke="#3db04b" stroke-width="3" stroke-linejoin="round"/></svg></div>
  <h2>Underground Locating</h2>
  <p>Lorem ipsum dolor sit amet adipis ing elit.Morbi ut elipsum tristique acc umsan. Morbi ut elit utipsum tristiquea Pellentesque habitant morbi.</p>
</section>

<div class="abs divider"></div>

<h2 class="abs col-head" style="left:59px">SPECIALS</h2>
<div class="abs specials-img" role="img" aria-label="Hand holding an LED bulb"></div>
<p class="abs specials-text">Lorem ipsuiim dolor sit amet, consectietur adipisic ing elit, sed do eiusmod tempor incididunt ut labo re et dolore magna aliqua.<br>Dolor sit amet, consectetur adipisicing elit, sed do eiusmod tempor incididunt ut labore et dolore ma gna aliqua. Ut enim ad minim veniam.</p>

<h2 class="abs col-head" style="left:303px">LATEST NEWS</h2>
<article class="abs news" style="top:795px"><div class="thumb" role="img" aria-label="Hands typing on a keyboard"></div><h3>Huntsville Etiam adipis</h3><p>May 31, 2013 by Reese<br>Suspendisse eu eriatin quam. iva<br>mus porttitor eros quis nisi lacini</p></article>
<article class="abs news" style="top:867px"><div class="thumb" role="img" aria-label="Laptop on an office desk"></div><h3>Buntsville Rtiam adipis</h3><p>May 31, 2013 by Reese<br>Suspendisse eu eriatin quam. iva<br>mus porttitor eros quis nisi lacini</p></article>
<article class="abs news" style="top:938px"><div class="thumb" role="img" aria-label="Office worker at a computer"></div><h3>Suntsville Utiam edipis</h3><p>May 31, 2013 by Reese<br>Suspendisse eu eriatin quam. iva<br>mus porttitor eros quis nisi lacini</p></article>

<h2 class="abs col-head" style="left:550px">TESTMONIALS</h2>
<blockquote class="abs quote-box">Fusce feugiat malesuada odio. Morbi nunc do gravida at, cursus nec, luctus a, lorem. Maecn as tristique orci acd sem. Lorem ipsum dolorsi t amet, consectetur adipisicing elit, sed do eiu smod tempor</blockquote>
<svg class="abs quote-tail" width="30" height="16" viewBox="0 0 30 16"><path d="M0 0h30L0 16z" fill="#ececec"/></svg>
<div class="abs portrait" role="img" aria-label="Portrait of a client"></div>
<p class="abs cite">Maecenintty interu coquat sit amet, consectetur</p>
<div class="abs cite-name"><svg width="10" height="10" viewBox="0 0 10 10"><circle cx="5" cy="3" r="2.6" fill="#333"/><path d="M0 10c0-4 10-4 10 0z" fill="#333"/></svg>Dean Porter's</div>

<footer class="abs footer">
  <div class="fcol" style="left:60px"><b>COMPANY</b><b>About</b><b>Contact</b><b>Legals &amp; Privacy</b><b>Niptaiades Keuytaser</b><b>Nemosera Lasecaerat</b></div>
  <div class="fcol" style="left:209px"><b>MORE</b><b>How it Works</b><b>FAQ</b><b>Media Centre</b><b>Suggest a Business</b><b>Blog</b></div>
  <div class="fcol" style="left:345px"><b>SPECIAL OFFERS</b><b>Media Owners</b><b>Marketing Providers</b><b>Nemosera Lasecaerat</b><b>Binsequuntur</b><b>Dolar ipsum</b></div>
  <div class="accred">PROUDLY ACCREDITED GREENVOLT ELECTRICIANS<div class="badge" role="img" aria-label="Accreditation badge"></div></div>
  <div class="social">Connect with us
    <div class="row"><span class="sq" style="background:#3b5998"></span>Folkpage</div>
    <div class="row"><span class="sq" style="background:#cb2027"></span>Pinspire</div>
    <div class="row"><span class="sq" style="background:#2aa9e0"></span>Chirper</div>
  </div>
</footer>
<div class="abs footer-base"><span class="abs" style="left:58px;top:13px">Copyrights 2013. All Rights Reserved.</span><span class="abs" style="left:779px;top:16px;font-size:8px">X4</span></div>

</body>
</html>
```